Drone services brochure, offering revolutionary new SkyTally service.

We need a 8.5 x 11 tri-fold that opens up into THREE 8.5 x 11 pages (all connected as a tri-fold, of course). The trifold is going to be a sales tool we will use to sell our services to commercial roofing contractors. We want the cover of the trifold to really catch the attention or intrigue a roofing professional who we'd be pitching the service to, see the file titled "commercial cover example.png" so you get an idea of what I'm referring to The logos for Summit Lensworks and SkyTally should be next to each other, and at the TOP of the page on the cover page. All the content required is included in the file uploads, including the photos we want to use and also the written text to go with the photos. Please see the file title "Commercial-roofing SkyTally Brochure INSTRUCTIONS" for clear instructions as to what text goes where and with which photos, also see trifold examples 1-3 that give you an idea as to how I envision the layout, and finally see the actual trifold examples of a completed trifold. Finally, you will notice that all these photos are sample photos, I have not yet purchased the rights to these photos simply because I need to make sure that 1) there's enough room and 2)these are actually the photos we want to use. Once the design is set, then I'll purchase the files and send them to the designer.

Target Market(s)

Commercial roofing contractors are going to be who read/see the trifold.

Industry/Entity Type

Sales

Font styles to use
Serif

Colors
0555a3
f37022
34a6d7

Requirements
Must have
• Project must have a clean look to it that is easy on the eyes, especially the cover.
Nice to have
• I would be nice to fit all the pictures i included, even if they are minimized in size a bit.

```html
<!DOCTYPE html>
<html lang="en">
<head>
<meta charset="utf-8">
<title>SkyTally Tri-fold Brochure</title>
<link href="https://fonts.googleapis.com/css2?family=Open+Sans:wght@400;600;700&family=PT+Serif:wght@400;700&display=swap" rel="stylesheet">
<style>
  :root{
    --canvas:#e6e6e6;
    --paper:#ffffff;
    --ink:#333333;
    --dark:#2a2a2c;
    --dark-2:#3a3a3d;
    --accent:#1e9ad8;
    --accent-deep:#0c7fc1;
    --orange:#f37022;
    --white:#ffffff;
  }
  html,body{margin:0;padding:0;width:901px;height:1200px;overflow:hidden;background:var(--canvas);}
  body{position:relative;font-family:"Open Sans",Arial,sans-serif;color:var(--ink);}
  .trifold{position:absolute;left:20px;top:268px;width:725px;height:560px;transform:scale(1.1876);transform-origin:0 0;
    box-shadow:0 3px 10px rgba(0,0,0,.25);overflow:hidden;background:var(--paper);}
  .backdrop{position:absolute;inset:0;width:725px;height:560px;}
  .abs{position:absolute;margin:0;}
  .serif{font-family:"PT Serif",Georgia,serif;}
  .headline{font-family:"PT Serif",Georgia,serif;color:var(--accent);font-weight:700;font-size:11.5px;line-height:13px;}
  .body-copy{font-size:6.6px;line-height:8.6px;color:#3a3a3a;}
  .section-title{font-family:"PT Serif",Georgia,serif;color:var(--accent);font-weight:700;font-size:14px;letter-spacing:.3px;}
  .on-dark{color:#f1f1f1;}
  .justify{text-align:justify;}
  .follow{font-size:8px;color:#333;display:flex;align-items:center;gap:3px;}
  .dot-icon{width:11px;height:11px;border-radius:50%;background:var(--accent);display:inline-block;}
  .contact{font-size:12px;color:var(--white);display:flex;align-items:center;gap:7px;}
  .contact svg{flex:none;}
  .cover-pitch{font-family:"PT Serif",Georgia,serif;color:var(--white);text-align:right;font-weight:700;line-height:1.08;}
  .cover-pitch span{display:block;}
  .cover-pitch .sm{font-size:8.5px;}
  .cover-pitch .md{font-size:13px;}
  .cover-pitch .lg{font-size:20px;}
  .brand-row{display:flex;align-items:center;justify-content:space-between;box-sizing:border-box;padding:0 12px;}
  .brand{display:flex;align-items:center;gap:5px;font-family:"PT Serif",Georgia,serif;color:var(--white);font-weight:700;font-size:13px;}
  .brand .mark{width:9px;height:9px;background:var(--orange);flex:none;}
  .tagline{text-align:center;font-size:8px;line-height:11px;}
  .tagline strong{color:var(--accent);font-weight:700;}
  .tagline span{color:var(--white);}
</style>
</head>
<body>
<main class="trifold">
  <svg class="backdrop" viewBox="0 0 725 560" aria-hidden="true">
    <defs>
      <linearGradient id="mid-paper" x1="0" y1="0" x2="1" y2="0">
        <stop offset="0" stop-color="#e4e4e4"/><stop offset=".25" stop-color="#fafafa"/><stop offset="1" stop-color="#ffffff"/>
      </linearGradient>
    </defs>
    <rect x="0" y="0" width="242" height="560" fill="#ffffff"/>
    <rect x="242" y="0" width="243" height="560" fill="url(#mid-paper)"/>
    <polygon points="0,322 300,476 485,420 485,560 0,560" fill="var(--dark)"/>
    <polygon points="0,316 302,470 302,478 0,324" fill="var(--accent)"/>
    <polygon points="292,480 485,414 485,422 300,482" fill="var(--accent)"/>
    <rect x="485" y="0" width="240" height="560" fill="var(--dark)"/>
    <polygon points="485,385 725,440 725,560 485,560" fill="var(--dark-2)" opacity=".55"/>
    <polygon points="485,345 725,255 725,440 485,388" fill="var(--accent)"/>
    <polygon points="485,388 725,440 725,446 485,394" fill="var(--accent-deep)"/>
    <rect x="485" y="40" width="240" height="2" fill="var(--orange)"/>
  </svg>

  <!-- cover photo -->
  <div class="abs" role="img" aria-label="Aerial photo of commercial flat rooftops with a quadcopter drone hovering above"
       style="left:485px;top:42px;width:240px;height:303px;clip-path:polygon(0 0,100% 0,100% 70%,0 100%);
       background:linear-gradient(160deg,#6f767c 0%,#b9bec2 35%,#d6d9db 55%,#5b6166 80%,#2f3235 100%);"></div>

  <!-- LEFT PANEL -->
  <h2 class="abs headline" style="left:15px;top:20px;width:215px;">LOREM IPSUM DOLOR SIT AMET, CONSECTETUR ADIPISCING ELIT</h2>
  <p class="abs body-copy justify" style="left:15px;top:56px;width:212px;">Sed do eiusmod tempor incididunt ut labore et dolore magna aliqua. Ut enim ad minim veniam, quis nostrud exercitation ullamco laboris nisi ut aliquip ex ea commodo consequat. Duis aute irure dolor in reprehenderit in voluptate velit esse cillum</p>

  <div class="abs" role="img" aria-label="Drone carrying a cardboard parcel against a blue sky"
       style="left:16px;top:136px;width:90px;height:90px;border-radius:50%;border:2px solid var(--accent);box-sizing:border-box;
       background:radial-gradient(circle at 50% 60%,#d9b27a 0 18%,#7fb6e6 20%,#2f6fb8 100%);"></div>
  <p class="abs body-copy" style="left:116px;top:142px;width:118px;">Sed do eiusmod tempor incididunt ut labore et dolore magna aliqua. Ut enim ad minim veniam, quis nostrud exercitation ullamco laboris nisi ut aliquip ex ea commodo consequat. Duis aute irure dolor in reprehenderit in voluptate velit esse cillum</p>

  <p class="abs body-copy" style="left:15px;top:246px;width:118px;">Sed do eiusmod tempor incididunt ut labore et dolore magna aliqua. Ut enim ad minim veniam, quis nostrud exercitation ullamco laboris nisi ut aliquip ex ea commodo consequat. Duis aute irure dolor in reprehenderit in voluptate velit esse cillum</p>
  <div class="abs" role="img" aria-label="Row of small figures with one highlighted, on a teal backdrop"
       style="left:139px;top:238px;width:84px;height:84px;border-radius:50%;border:2px solid var(--accent);box-sizing:border-box;
       background:radial-gradient(circle at 40% 40%,#bfe3e6,#3f9aa3 60%,#1d5e66);"></div>
  <div class="abs" role="img" aria-label="Five gold rating stars"
       style="left:125px;top:336px;width:100px;height:28px;border-radius:4px;
       background:linear-gradient(90deg,#f3d37a,#e0a727 50%,#f3d37a);opacity:.9;"></div>

  <h2 class="abs section-title" style="left:15px;top:382px;">WE OFFER</h2>
  <p class="abs body-copy on-dark" style="left:15px;top:406px;width:205px;">our services with safety first, flexibility second. This<br>means that our FAA licensed pilots fly<br>only within the confines of regulations and<br>only under safe flying conditions. This also means<br>that we are responsible for all permits or permissions<br>required to fly as well as a minimum of $1M insurance, and of<br>course all the equipment to go with. We are a turn-key<br>service to help you gain the edge on your competitor with a<br>service that is set to change the approach to commercial<br>roofing. We can adjust flight plans and data collection to<br>your company's inspection protocols to make sure<br>we are collecting the data that is valuable to you<br>and will give your team and edge the<br>competitor does not have.</p>

  <!-- MIDDLE PANEL -->
  <div class="abs" role="img" aria-label="Jigsaw puzzle with a red piece labelled data"
       style="left:270px;top:18px;width:180px;height:180px;border-radius:50%;border:3px solid var(--accent);box-sizing:border-box;
       background:radial-gradient(circle at 50% 35%,#d8473a 0 13%,#f2f2f2 15%,#cfcfcf 70%,#9c9c9c 100%);"></div>
  <div class="abs" role="img" aria-label="Metal gears engraved with quality themes"
       style="left:368px;top:156px;width:98px;height:98px;border-radius:50%;border:2px solid var(--accent);box-sizing:border-box;
       background:radial-gradient(circle at 45% 45%,#e0e0e0,#7a7a7a 55%,#2e2e2e);"></div>

  <h2 class="abs section-title" style="left:260px;top:262px;">ABOUT US</h2>
  <p class="abs body-copy justify" style="left:260px;top:286px;width:209px;">Summit Lensworks is a network of licensed, skilled, and insured drone pilots. The founders Mateo Ruelas and Casey Whitford both have a background in the photovoltaic industry specific to system design and implementation. The use of drones for both Mateo and Casey goes back to 2014 when the technology was first implemented to estimate solar panel installations. Now Summit Lensworks has grown to offer estimating services for solar installation as well as residential and commercial roof estimating.</p>
  <div class="abs follow" style="left:260px;top:423px;">FOLLOW US ON <span class="dot-icon"></span><span class="dot-icon"></span></div>

  <h2 class="abs section-title" style="left:356px;top:486px;font-size:12.5px;">GET IN TOUCH</h2>
  <div class="abs contact" style="left:268px;top:512px;">
    <svg width="7" height="6" viewBox="0 0 7 6"><rect x=".5" y=".5" width="6" height="5" fill="none" stroke="#1e9ad8"/><path d="M.5 .5 3.5 3 6.5 .5" fill="none" stroke="#1e9ad8"/></svg>
    info@summitlensworks.net</div>
  <div class="abs contact" style="left:268px;top:532px;">
    <svg width="7" height="7" viewBox="0 0 7 7"><circle cx="3.5" cy="3.5" r="3" fill="#1e9ad8"/></svg>
    www.summitlensworks.net</div>

  <!-- COVER PANEL -->
  <div class="abs brand-row" style="left:485px;top:12px;width:240px;">
    <div class="brand"><span class="mark"></span>SkyTally</div>
    <div class="brand"><span class="mark"></span>Summit Lensworks</div>
  </div>
  <p class="abs cover-pitch" style="right:8px;top:300px;">
    <span class="md">A COMPETITIVE</span>
    <span class="lg" style="font-size:16px;">ADVANTAGE IN</span>
    <span class="sm">COMMERCIAL ROOFING WITH</span>
    <span class="md" style="font-size:14px;">ON-DEMAND DRONE</span>
    <span class="md">IMAGERY IN</span>
    <span class="lg">2018</span>
  </p>
  <div class="abs tagline" style="left:485px;top:505px;width:240px;">
    <strong>"A VETERAN-OWNED BUSINESS"</strong><br><span>Lakeview Business Chamber</span>
  </div>
</main>
</body>
</html>
```